Commercial construction contractor website.

We need a website that contains About Us, Contact info, Services, Project pictures and Industry News section

Target Market(s)

I'm building industral/flex spaces/commercial.

Industry/Entity Type

Commercial/industrial construction

Coding

Coded - Design and coding required

Number of Pages Required

5+ page

Font styles to use
Other font styles liked:
• The logo font is Microgramma Pro

Requirements
Must have
• Must have correct company name spelling: Dunmore Ridge Construction
Nice to have
• I do like to see our logo design implemented in the design
Should not have
• Please do not show big city pictures and business suit people. We are a commercial construction company

```html
<!DOCTYPE html>
<html lang="en">
<head>
<meta charset="utf-8">
<title>Dunmore Ridge Construction</title>
<link href="https://fonts.googleapis.com/css2?family=Krona+One&family=Poppins:wght@400;500;600&display=swap" rel="stylesheet">
<style>
:root{
  --blue-dark:#0b3f8f;
  --blue:#0a5fb0;
  --blue-light:#0b7cc4;
  --ink:#3a3a3a;
  --text:#4a4a4a;
  --grey-light:#ececec;
  --footer:#5d5d60;
  --footer-dark:#4e4e51;
  --white:#ffffff;
}
*{margin:0;padding:0;box-sizing:border-box}
html,body{width:1200px;height:4229px;overflow:hidden;background:var(--white)}
body{position:relative;font-family:"Poppins",sans-serif;color:var(--text)}
.abs{position:absolute}
.display{font-family:"Krona One",sans-serif;color:var(--ink);line-height:1.1}
svg.layer{position:absolute;left:0;top:0}

/* nav */
.brand{left:89px;top:62px;width:164px;text-align:center;font-family:"Krona One",sans-serif;color:#5a5a5a}
.brand .name{font-size:14px;letter-spacing:.5px;display:block}
.brand .sub{font-size:8px;letter-spacing:1px;display:block;border-top:1px solid #888;margin-top:3px;padding-top:2px;color:var(--blue-dark)}
.nav{top:28px;left:690px;display:flex;align-items:center;gap:26px;font-size:12px;color:#333}
.nav .contact{border:2px solid var(--blue-dark);padding:7px 22px;margin-left:4px}

/* hero */
.eyebrow{left:89px;top:312px;font-family:"Krona One",sans-serif;font-size:23px;color:var(--blue-dark)}
.hero-title{left:87px;top:340px;font-size:52px}
.hero-copy{left:89px;top:452px;width:450px;font-size:13px;line-height:22px;color:#555}
.btn-solid{left:89px;top:509px;width:154px;height:38px;background:var(--blue);color:#fff;font-size:12px;font-weight:600;display:flex;align-items:center;justify-content:center;letter-spacing:.3px}

/* about */
.about-title{left:642px;top:930px;font-size:35px}
.about-copy{left:642px;top:1024px;width:475px;font-size:14px;line-height:25px;color:#555}
.btn-outline{left:642px;top:1144px;width:126px;height:36px;border:2px solid var(--blue-dark);color:#222;font-size:12px;font-weight:600;display:flex;align-items:center;justify-content:center}

/* services band */
.services-title{width:1200px;text-align:center;font-size:38px}
.on-blue{color:#fff}
.svc{width:310px;color:#fff}
.svc h3{font-family:"Krona One",sans-serif;font-size:16px;font-weight:400;margin:8px 0 10px}
.svc p{font-size:14px;line-height:26px}
.svc.left{text-align:right}
.svc svg{display:inline-block}

/* footer */
.foot-col h4{font-family:"Krona One",sans-serif;font-size:19px;font-weight:400;color:#fff;margin-bottom:12px}
.foot-col{font-size:12px;color:#fff;line-height:23px}
.foot-brand{left:110px;top:4047px;width:246px;text-align:center;font-family:"Krona One",sans-serif;color:#fff}
</style>
</head>
<body>

<!-- background shapes -->
<svg class="layer" width="1200" height="4229" viewBox="0 0 1200 4229" aria-hidden="true">
  <defs>
    <linearGradient id="blueGrad" x1="0" y1="1" x2="1" y2="0">
      <stop offset="0" stop-color="#0a3a88"/>
      <stop offset="1" stop-color="#0b7fc6"/>
    </linearGradient>
    <linearGradient id="bandGrad" x1="0" y1="0" x2="1" y2="0.4">
      <stop offset="0" stop-color="#0a3e8c"/>
      <stop offset=".55" stop-color="#0a5cad"/>
      <stop offset="1" stop-color="#0b7cc4"/>
    </linearGradient>
    <linearGradient id="heroPhoto" x1="0" y1="0" x2="0" y2="1">
      <stop offset="0" stop-color="#8fb9d8"/>
      <stop offset=".45" stop-color="#a7a9a6"/>
      <stop offset=".75" stop-color="#8a7a62"/>
      <stop offset="1" stop-color="#b2926a"/>
    </linearGradient>
    <linearGradient id="aboutPhoto" x1="0" y1="0" x2="1" y2="1">
      <stop offset="0" stop-color="#c9c9c4"/>
      <stop offset=".5" stop-color="#9b7a5b"/>
      <stop offset="1" stop-color="#6d7d4b"/>
    </linearGradient>
  </defs>

  <!-- hero frame + photo -->
  <polygon points="886,62 1200,240 1200,640 1120,600 1200,560 1200,260" fill="url(#blueGrad)"/>
  <polygon points="1040,150 1200,70 1200,210 1100,260 980,200" fill="url(#blueGrad)"/>
  <polygon points="1020,620 1200,520 1200,700 1100,760" fill="url(#blueGrad)"/>
  <polygon points="886,69 1200,249 1200,606 886,788 578,624 578,246" fill="url(#heroPhoto)" role="img" aria-label="Photo: two construction workers in hard hats and safety vests inspecting a steel frame"/>
  <polygon points="940,250 1080,170 1200,240 1200,320 1080,250 990,300" fill="#1a6fd0" opacity=".85"/>

  <!-- about frame + photo -->
  <polygon points="312,739 575,891 575,1272 540,1250 540,910 312,780 85,910 85,1190 49,1190 49,891" fill="url(#blueGrad)"/>
  <polygon points="317,763 550,897 550,1174 317,1308 85,1174 85,897" fill="url(#aboutPhoto)" role="img" aria-label="Photo: construction worker climbing scaffolding"/>

  <!-- services band -->
  <polygon points="0,1412 85,1330 328,1466 484,1376 629,1473 1200,1195 1200,1965 0,2323" fill="url(#bandGrad)"/>
  <polygon points="624,2126 1200,1965 1200,2279" fill="var(--grey-light)"/>

  <!-- project hex grid -->
  <g>
    <polygon points="345,2372 466,2442 466,2581 345,2651 224,2581 224,2442" fill="#b9bcbf" role="img" aria-label="Photo: empty industrial warehouse interior"/>
    <polygon points="599,2372 720,2442 720,2581 599,2651 478,2581 478,2442" fill="#8d7a5a" role="img" aria-label="Photo: meeting room with long table"/>
    <polygon points="857,2372 978,2442 978,2581 857,2651 736,2581 736,2442" fill="#9ea3a6" role="img" aria-label="Photo: office with glass partitions"/>
    <polygon points="213,2594 334,2664 334,2803 213,2873 92,2803 92,2664" fill="#c9cbcd" role="img" aria-label="Photo: white corridor with glass doors"/>
    <polygon points="469,2594 590,2664 590,2803 469,2873 348,2803 348,2664" fill="#9c8f82" role="img" aria-label="Photo: worker fitting a steel frame at sunset"/>
    <polygon points="727,2594 848,2664 848,2803 727,2873 606,2803 606,2664" fill="#5e6266" role="img" aria-label="Photo: flex space interior under construction"/>
    <polygon points="985,2594 1106,2664 1106,2803 985,2873 864,2803 864,2664" fill="#b7b4ae" role="img" aria-label="Photo: open office with concrete columns"/>
    <polygon points="706,2710 724,2720 724,2742 706,2752 688,2742 688,2720" fill="#fff"/>
    <circle cx="705" cy="2730" r="5" fill="none" stroke="#555" stroke-width="1.5"/>
    <line x1="709" y1="2734" x2="713" y2="2738" stroke="#555" stroke-width="1.5"/>
    <polygon points="747,2710 765,2720 765,2742 747,2752 729,2742 729,2720" fill="#fff"/>
    <path d="M742 2736 l10 -10 M740 2732 l4 -4 a3 3 0 0 1 4 4 M754 2730 l-4 4 a3 3 0 0 1 -4 -4" stroke="#555" stroke-width="1.5" fill="none"/>
  </g>

  <!-- testimonial quote mark -->
  <text x="84" y="3240" font-family="Krona One, sans-serif" font-size="240" fill="#ececec">&#8220;</text>

  <!-- client photo circles -->
  <g>
    <circle cx="875" cy="3001" r="36" fill="#c9a2d8" role="img" aria-label="Client portrait"/>
    <circle cx="1070" cy="3075" r="32" fill="#d9b898" role="img" aria-label="Client portrait"/>
    <circle cx="760" cy="3185" r="82" fill="#e6567a" role="img" aria-label="Client portrait"/>
    <circle cx="998" cy="3185" r="28" fill="#e9a8b8" role="img" aria-label="Client portrait"/>
    <circle cx="1169" cy="3280" r="49" fill="#f0c33a" role="img" aria-label="Client portrait"/>
    <circle cx="998" cy="3342" r="62" fill="#b98556" role="img" aria-label="Client portrait"/>
    <circle cx="850" cy="3374" r="36" fill="#5fb9b5" role="img" aria-label="Client portrait"/>
    <circle cx="882" cy="3505" r="20" fill="#6e6e6e" role="img" aria-label="Client portrait"/>
    <circle cx="1090" cy="3518" r="33" fill="#d2d2d2" role="img" aria-label="Client portrait"/>
  </g>

  <!-- footer -->
  <polygon points="0,3948 400,3771 1200,3907 1200,4229 0,4229" fill="var(--footer)"/>
  <line x1="89" y1="4181" x2="1111" y2="4181" stroke="#777" stroke-width="1"/>
  <circle cx="1139" cy="4176" r="20" fill="var(--blue)"/>
  <path d="M1133 4179 l6 -6 l6 6" stroke="#fff" stroke-width="2" fill="none"/>
</svg>

<!-- nav -->
<div class="abs brand"><span class="name">DUNMORE RIDGE</span><span class="sub">CONSTRUCTION</span></div>
<nav class="abs nav">
  <svg width="14" height="13" viewBox="0 0 14 13" aria-label="Home"><path d="M7 0 L14 6 H12 V13 H8.5 V9 H5.5 V13 H2 V6 H0 Z" fill="var(--blue)"/></svg>
  <span>ABOUT US</span><span>SERVICES</span><span>PROJECT</span><span class="contact">CONTACT US</span>
</nav>

<!-- hero -->
<div class="abs eyebrow">Flexible space</div>
<h1 class="abs display hero-title">Actions.<br>Not Words.</h1>
<p class="abs hero-copy">We are a general contractor that believes in setting clear expecta-<br>tions and delivering on our commitments.</p>
<div class="abs btn-solid">VIEW PROJECTS</div>

<!-- about -->
<h2 class="abs display about-title">About Dunmore<br>Ridge Construction</h2>
<p class="abs about-copy">Lorem Ipsum is simply dummy text of the printing and typeset­ting industry. Lorem Ipsum has been the industry's standard dummy text ever since the 1500s, when an unknown printer took a galley of type and scrambled it to .</p>
<div class="abs btn-outline">READ MORE</div>

<!-- services -->
<h2 class="abs display services-title on-blue" style="top:1585px">Our Services</h2>

<div class="abs svc left" style="left:87px;top:1650px">
  <svg width="60" height="58" viewBox="0 0 60 58" fill="none" stroke="#fff" stroke-width="2"><rect x="6" y="14" width="20" height="40"/><path d="M10 20h4M18 20h4M10 28h4M18 28h4M10 36h4M18 36h4"/><path d="M6 14 L16 4 L26 14"/><circle cx="44" cy="30" r="10"/><circle cx="44" cy="30" r="4"/><path d="M28 54h28V42"/></svg>
  <h3>Construction Management</h3>
  <p>Lorem Ipsum is simply dummy text of the printing and typesetting industry.</p>
</div>
<div class="abs svc left" style="left:87px;top:1818px">
  <svg width="54" height="50" viewBox="0 0 54 50" fill="none" stroke="#fff" stroke-width="2"><rect x="4" y="2" width="26" height="46"/><rect x="30" y="22" width="20" height="26"/><path d="M11 10h4M19 10h4M11 18h4M19 18h4M11 26h4M19 26h4M37 30h6M37 38h6"/></svg>
  <h3>Commercial</h3>
  <p>Lorem Ipsum is simply dummy text of the printing and typesetting industry.</p>
</div>
<div class="abs svc" style="left:795px;top:1650px">
  <svg width="60" height="58" viewBox="0 0 60 58" fill="none" stroke="#fff" stroke-width="2"><circle cx="30" cy="30" r="24"/><rect x="16" y="24" width="10" height="22"/><rect x="28" y="16" width="10" height="30"/><rect x="40" y="30" width="6" height="16"/><path d="M8 46h44"/></svg>
  <h3>Industrial construction</h3>
  <p>Lorem Ipsum is simply dummy text of the printing and typesetting industry.</p>
</div>
<div class="abs svc" style="left:795px;top:1820px">
  <svg width="56" height="50" viewBox="0 0 56 50" fill="none" stroke="#fff" stroke-width="2"><path d="M4 10 L26 4 V46 L4 40 Z"/><path d="M30 4 L52 10 V40 L30 46 Z"/><path d="M10 14v22M46 14v22"/></svg>
  <h3>Flex spaces</h3>
  <p>Lorem Ipsum is simply dummy text of the printing and typesetting industry.</p>
</div>

<h2 class="abs display services-title" style="top:2298px">Our Services</h2>

<!-- testimonial -->
<h2 class="abs display" style="left:87px;top:3142px;font-size:35px">What our client’s<br>say about us</h2>
<p class="abs" style="left:89px;top:3243px;width:540px;font-size:18px;line-height:28.5px;color:#444">Lorem Ipsum is simply dummy text of the printing and type­setting industry. Lorem Ipsum has been the industry's stand­ard dummy text ever since the 1500s, when an unknown printer took a galley of type and scrambled it to make a type specimen book.</p>
<div class="abs" style="left:89px;top:3397px;font-size:15px;font-weight:600;color:var(--blue);letter-spacing:.5px">MARCUS HALE</div>
<svg class="abs" style="left:88px;top:3444px" width="82" height="20" viewBox="0 0 82 20" aria-label="Previous and next"><path d="M2 10h22M2 10l7-6M2 10l7 6" stroke="#999" stroke-width="1.5" fill="none"/><path d="M38 10h42M80 10l-7-6M80 10l-7 6" stroke="#222" stroke-width="2" fill="none"/></svg>

<!-- contact band -->
<div class="abs" style="left:89px;top:3633px;width:1022px;height:138px;background:linear-gradient(90deg,var(--blue-dark),var(--blue-light))">
  <div class="abs" style="left:49px;top:45px;font-family:'Krona One',sans-serif;font-size:29px;color:#fff">Contact us for commercial</div>
  <div class="abs" style="left:49px;top:82px;font-size:17px;color:#fff">and industrial design &amp; construction services</div>
  <div class="abs" style="left:811px;top:52px;width:167px;height:38px;background:#fff;color:#222;font-size:13px;font-weight:500;display:flex;align-items:center;justify-content:center">CONTACT US</div>
</div>

<!-- footer -->
<div class="abs foot-brand"><div style="font-size:21px;letter-spacing:.5px">DUNMORE RIDGE</div><div style="font-size:12px;letter-spacing:1px;border-top:2px solid #fff;margin-top:4px;padding-top:3px">CONSTRUCTION</div></div>
<div class="abs foot-col" style="left:423px;top:3930px">
  <h4>Useful Links</h4>
  <div>Home</div><div>About Us</div><div>Services</div><div>Project</div><div>News</div><div>Contact Us</div>
</div>
<div class="abs foot-col" style="left:625px;top:3930px">
  <h4>Newsletter</h4>
  <div>Subscribe to our newsletter</div>
  <div style="margin-top:6px;width:199px;height:31px;background:#fff;color:#888;font-size:11px;padding-left:14px;line-height:31px">Email Address</div>
  <div style="margin-top:8px;width:109px;height:28px;background:var(--blue-dark);font-size:11px;font-weight:600;text-align:center;line-height:28px">SUBSCRIBE</div>
</div>
<div class="abs foot-col" style="left:918px;top:3930px">
  <h4>Contact Us</h4>
  <div>Some goes address here</div><div>info@dunmoreridge.com</div><div>+1 555 014 2290</div>
  <div style="display:flex;gap:12px;margin-top:8px" aria-label="Social links">
    <span style="width:10px;height:10px;background:#fff;border-radius:50%"></span>
    <span style="width:10px;height:10px;background:#fff;border-radius:50%"></span>
    <span style="width:10px;height:10px;background:#fff;border-radius:50%"></span>
    <span style="width:10px;height:10px;background:#fff;border-radius:50%"></span>
  </div>
</div>
<div class="abs" style="left:0;top:4196px;width:1200px;text-align:center;font-size:13px;color:#fff">©Copyright 2022 | All Rights Reserved</div>

</body>
</html>
```